International Fundraising Consultancy needs a new PowerPoint Design

We train international nonprofits on how to fundraise globally. We plan to keep our current logo design and color, as we love the color orange, but want a cleaner, fresher, less cluttered template for our PowerPoint presentations. The finished product needs to be easy to edit, and include template slides that can feature tables, graphics and images. We would like a color scheme for graphics.The layout should be lighter, clear, attractive and easy to read and understand. We also want to use the same template for webinar slides. We have attached an example of our current PowerPoint template with identifying client information removed. The green slide that looks like a clapperboard fro a film is basically just a placeholder that indicates a break for an interactive exercise.

Target Market(s)

Board members, staff members, museum executives, leadership of NGOs, top businesspeople in Europe, many with a modern sense of aesthetics in the art world

Industry/Entity Type

Cleaner

Font styles to use
Sans Serif

Colors
f78f20
f37022

Requirements
Must have
• Orange colors, keep our Vormkelingen logo
• Good templates for tables, photos and graphics

```html
<!DOCTYPE html>
<html lang="en">
<head>
<meta charset="utf-8">
<title>Agenda – Vormkelingen &amp; Associates</title>
<link rel="stylesheet" href="https://fonts.googleapis.com/css2?family=Exo+2:wght@400;500;600;700&display=swap">
<style>
  :root {
    --orange: #e78f29;
    --orange-deep: #f37022;
    --bullet: #c96b48;
    --grey: #6d6e71;
    --ink: #1d1d1b;
    --paper: #ffffff;
  }
  * { margin: 0; padding: 0; box-sizing: border-box; }
  html, body { width: 1200px; height: 849px; overflow: hidden; background: var(--paper); }
  body { font-family: "Exo 2", sans-serif; color: var(--ink); }

  .slide { position: relative; width: 1200px; height: 849px; overflow: hidden; background: var(--paper); }

  .header-rule { position: absolute; left: 134px; top: 0; width: 6px; height: 86px; background: var(--orange); }
  .header-title { position: absolute; left: 162px; top: 36px; font-size: 20px; font-weight: 500; color: var(--orange); letter-spacing: 0.2px; }
  .header-date { position: absolute; left: 162px; top: 62px; font-size: 18px; font-weight: 500; color: var(--grey); }
  .header-date strong { font-weight: 700; }

  .slide-title { position: absolute; left: 129px; top: 150px; font-size: 58px; font-weight: 700; color: var(--grey); line-height: 1; }

  .agenda { position: absolute; left: 128px; top: 244px; width: 740px; list-style: none; }
  .agenda-item { position: relative; padding-left: 39px; font-size: 19.5px; line-height: 25.5px; color: var(--ink); margin-bottom: 33px; }
  .agenda-item::before {
    content: ""; position: absolute; left: 2px; top: 6px;
    width: 14px; height: 14px; border-radius: 50%; background: var(--bullet);
  }

  .footer-band { position: absolute; left: 0; top: 0; }
  .brand { position: absolute; left: 114px; top: 748px; display: flex; align-items: center; gap: 12px; }
  .brand-dot { width: 22px; height: 22px; border-radius: 50%; background: var(--orange); }
  .brand-name { font-size: 20px; font-weight: 500; color: var(--orange); line-height: 1; }
  .brand-tagline { position: absolute; left: 148px; top: 774px; font-size: 11px; font-weight: 500; color: var(--orange); }

  .footer-url { position: absolute; left: 470px; top: 754px; font-size: 17px; font-weight: 600; color: var(--paper); }
  .page-number { position: absolute; left: 1005px; top: 753px; font-size: 18px; font-weight: 700; color: var(--paper); }
</style>
</head>
<body>
<main class="slide">
  <div class="header-rule"></div>
  <p class="header-title">PPT HEADING GOES HERE</p>
  <p class="header-date">FEB, <strong>2015</strong></p>

  <h1 class="slide-title">Agenda</h1>

  <ul class="agenda">
    <li class="agenda-item">US Corporation with 16 years Lease and Loan Management Software experience US Corporation with 16 years Lease and Loan Management Software experience</li>
    <li class="agenda-item">US Corporation with 16 years Lease and Loan Management Software experience US Corporation with 16 years Lease and L</li>
    <li class="agenda-item">US Corporation with 16 years Lease and</li>
    <li class="agenda-item">US Corporation with 16 years Lease and Loan Management Software experience US Corporation with 16 y</li>
    <li class="agenda-item">US Corporation with 16 years Lease and</li>
  </ul>

  <svg class="footer-band" width="1200" height="849" viewBox="0 0 1200 849" aria-hidden="true">
    <path d="M431 723 H990 Q1125 723 1168 849 H1076 Q1050 802 990 802 H431 Z" fill="var(--orange)"/>
  </svg>

  <div class="brand">
    <span class="brand-dot"></span>
    <span class="brand-name">Vormkelingen &amp; Associates</span>
  </div>
  <p class="brand-tagline">Fundraising Counsel</p>

  <p class="footer-url">www.vormkelingen.com</p>
  <p class="page-number">01</p>
</main>
</body>
</html>
```